Business Card Design

I am specialising in Designs, Drafting and Council approvals. From the idea to the full set of plans and other documents. Residential houses only.
I am located in Northern Beaches, Sydney where the sky is always blue :)
Tall Pine Drafting should be associated with light, modern house designs & with 3D drafting. I am positive person, that would like help every client through the demanding time of council paperwork.

The business card should be light blue, with white 3D sketch and white or black writing. Simple, modern and "happy"

Please don't hesitate to suggest something if you think so.

Thanks
Petra

Industry/Entity Type

House

Contact Information for Business Card

FRONT:

Tall Pine Drafting
Servicing Northern Beaches

Petra Lindqvist
tallpinedrafting@mailvista.com.au
0498 527 036
www.tallpinedrafting.com.au

BACK:

Design consultation
Plans Drafting
3D Visualisation
Council Approvals

```html
<!DOCTYPE html>
<html lang="en">
<head>
<meta charset="utf-8">
<title>Tall Pine Drafting – Business Card</title>
<link rel="stylesheet" href="https://fonts.googleapis.com/css2?family=Questrial&display=swap">
<style>
  :root {
    --sky: #80d3ef;
    --brand-blue: #1a72bd;
    --white: #ffffff;
  }
  html, body {
    margin: 0;
    padding: 0;
    width: 1200px;
    height: 742px;
    overflow: hidden;
    background: var(--sky);
  }
  .card {
    position: relative;
    width: 1200px;
    height: 742px;
    background: var(--sky);
    font-family: "Questrial", "Century Gothic", sans-serif;
    overflow: hidden;
  }
  .brand-name {
    position: absolute;
    left: 84px;
    top: 262px;
    width: 308px;
    height: 181px;
    margin: 0;
    display: flex;
    align-items: center;
    justify-content: center;
    text-align: center;
    color: var(--white);
    font-size: 44px;
    font-weight: 400;
    line-height: 1.15;
  }
  .divider {
    position: absolute;
    left: 464px;
    top: 184px;
    width: 3px;
    height: 378px;
    background: var(--white);
  }
  .details {
    position: absolute;
    left: 523px;
    top: 0;
    margin: 0;
  }
  .details p {
    position: absolute;
    left: 0;
    margin: 0;
    line-height: 1;
    white-space: nowrap;
    color: var(--white);
    font-size: 32px;
    letter-spacing: 0.3px;
  }
  .details .company {
    top: 254px;
    font-size: 44px;
    color: var(--brand-blue);
  }
  .details .tagline { top: 308px; font-size: 34px; }
  .details .email   { top: 396px; }
  .details .phone   { top: 440px; }
  .details .website { top: 483px; }
</style>
</head>
<body>
  <main class="card">
    <p class="brand-name">Tall Pine<br>Drafting</p>

    <div class="divider"></div>

    <div class="details">
      <p class="company">Tall Pine Drafting Servicing</p>
      <p class="tagline">Northern Beaches Petra Lindqvist</p>
      <p class="email">tallpinedrafting@mailvista.com.au</p>
      <p class="phone">0498 527 036</p>
      <p class="website">www.tallpinedrafting.com.au</p>
    </div>
  </main>
</body>
</html>
```